Pull Up Banners

Would like to have these pull up banner designs changed to a new modern theme. I have running a sales booth and want to re-design the banner designs. I have uploaded old banner design, I need phone number and website added onto bottom. Happy to consider images to attract people attention to increase sales and spark people interest walking past.

```html
<!DOCTYPE html>
<html lang="en">
<head>
<meta charset="utf-8">
<title>Kestrel Tech Pull Up Banners</title>
<link rel="stylesheet" href="https://fonts.googleapis.com/css2?family=Poppins:wght@400;600;700&family=Saira:wght@600;700&display=swap">
<style>
:root{
  --orange:#f26a21;
  --ink:#1c1e22;
  --dark:#1f2226;
  --dark-2:#15171a;
  --white:#ffffff;
  --page:#ececec;
  --label:#f3f3f3;
}
*{box-sizing:border-box;margin:0;padding:0}
html,body{width:1200px;height:1159px;overflow:hidden;background:var(--page)}
.canvas{position:relative;width:1200px;height:1159px}
.banner{position:absolute;top:24px;width:450px;height:1110px;overflow:hidden;box-shadow:0 4px 18px rgba(0,0,0,.12)}
.banner--cloud{left:100px}
.banner--managed{left:650px}
.banner__art{position:absolute;left:0;top:0;width:585px;height:1445px;transform:scale(.7692);transform-origin:0 0;
  background:linear-gradient(180deg,var(--dark) 0%,var(--dark) 60%,var(--dark-2) 100%);font-family:"Poppins",sans-serif;color:var(--white)}
.photo{position:absolute;left:0;top:170px;width:585px;height:580px}
.photo--cloud{background:
  radial-gradient(circle at 52% 46%,rgba(255,190,130,.85) 0,rgba(242,106,33,.45) 12%,rgba(60,50,45,0) 34%),
  radial-gradient(ellipse at 80% 30%,rgba(200,200,205,.35) 0,rgba(0,0,0,0) 45%),
  linear-gradient(180deg,#3a3634 0%,#2a2828 55%,var(--dark) 100%)}
.photo--managed{height:500px;background:
  radial-gradient(ellipse at 30% 20%,rgba(230,200,170,.55) 0,rgba(0,0,0,0) 45%),
  radial-gradient(ellipse at 55% 60%,rgba(210,215,220,.35) 0,rgba(0,0,0,0) 40%),
  radial-gradient(circle at 75% 75%,rgba(242,106,33,.35) 0,rgba(0,0,0,0) 25%),
  linear-gradient(180deg,#4a4440 0%,#2b2a2a 55%,var(--dark) 100%)}
.swoosh{position:absolute;left:0;top:0;width:585px;height:1445px}
.brand{position:absolute;left:0;top:52px;width:585px;display:flex;justify-content:center;align-items:center;gap:14px}
.brand__dot{width:50px;height:50px;border-radius:50%;background:var(--orange)}
.brand__text{display:flex;flex-direction:column}
.brand__name{font-family:"Poppins",sans-serif;font-weight:700;font-size:38px;line-height:1;color:var(--orange)}
.brand__tagline{font-family:"Poppins",sans-serif;font-weight:600;font-size:10px;letter-spacing:.6px;color:var(--ink);margin-top:4px}
.title-box{position:absolute;left:55px;width:475px;border:2px solid var(--orange);border-radius:14px}
.title{position:absolute;left:0;width:585px;text-align:center;font-family:"Saira",sans-serif;font-weight:700;font-size:54px;line-height:56px;letter-spacing:.5px;color:var(--white)}
.title span{background:var(--dark);padding:0 14px}
.service{position:absolute;width:250px;text-align:center}
.service__icon{width:70px;height:70px;border-radius:50%;background:var(--orange);margin:0 auto;display:flex;align-items:center;justify-content:center}
.service__label{margin-top:16px;font-weight:600;font-size:18px;line-height:28px;color:var(--label);white-space:nowrap}
.contact{position:absolute;left:0;top:1262px;width:585px;text-align:center;color:var(--ink)}
.contact__heading{display:flex;align-items:center;justify-content:center;gap:14px;font-weight:700;font-size:28px}
.contact__heading::before,.contact__heading::after{content:"";width:42px;height:2px;background:#9a9a9a}
.contact__phone{margin-top:4px;display:flex;align-items:center;justify-content:center;gap:10px;font-family:"Saira",sans-serif;font-weight:700;font-size:58px;line-height:66px;letter-spacing:1px}
.contact__web{font-size:24px;letter-spacing:.3px}
.contact__web b{font-weight:700}
</style>
</head>
<body>
<main class="canvas">

  <section class="banner banner--cloud">
    <div class="banner__art">
      <div class="photo photo--cloud" role="img" aria-label="Hands typing on a laptop with a glowing cloud and connected service icons"></div>
      <svg class="swoosh" viewBox="0 0 585 1445">
        <path d="M0 0H585V105Q292 305 0 105Z" fill="#fff"/>
        <path d="M0 105Q292 305 585 105V160Q292 270 0 160Z" fill="var(--orange)"/>
        <path d="M0 172Q292 282 585 172" fill="none" stroke="#fff" stroke-width="3"/>
        <path d="M0 1290Q292 1166 585 1290V1445H0Z" fill="var(--orange)"/>
        <path d="M0 1345Q292 1145 585 1345V1445H0Z" fill="#fff"/>
        <path d="M0 1280Q292 1160 585 1280" fill="none" stroke="#fff" stroke-width="3"/>
        <g fill="none" stroke="var(--orange)" stroke-width="2">
          <path d="M293 905V1085"/>
          <path d="M293 948Q293 975 268 975H210M293 948Q293 975 318 975H378"/>
          <path d="M293 1078Q293 1105 268 1105H210M293 1078Q293 1105 318 1105H378"/>
        </g>
        <g fill="var(--orange)">
          <circle cx="210" cy="975" r="4.5"/><circle cx="378" cy="975" r="4.5"/>
          <circle cx="210" cy="1105" r="4.5"/><circle cx="378" cy="1105" r="4.5"/>
        </g>
      </svg>
      <div class="brand">
        <div class="brand__dot"></div>
        <div class="brand__text">
          <span class="brand__name">KESTREL TECH</span>
          <span class="brand__tagline">SMART, RELIABLE SUPPORT FOR EVERY BUSINESS</span>
        </div>
      </div>
      <div class="title-box" style="top:765px;height:112px"></div>
      <h2 class="title" style="top:738px"><span>CLOUD</span><br>PHONE SYSTEM<br><span>&amp; INTERNET</span></h2>

      <div class="service" style="left:38px;top:940px">
        <div class="service__icon"><svg width="36" height="36" viewBox="0 0 24 24" fill="#fff"><path d="M6.6 10.8a15.1 15.1 0 006.6 6.6l2.2-2.2a1 1 0 011-.25 11.4 11.4 0 003.6.6 1 1 0 011 1V20a1 1 0 01-1 1A17 17 0 013 4a1 1 0 011-1h3.5a1 1 0 011 1c0 1.25.2 2.45.6 3.6a1 1 0 01-.25 1z"/></svg></div>
        <p class="service__label">VoIP &amp; Phone Systems</p>
      </div>
      <div class="service" style="left:300px;top:940px">
        <div class="service__icon"><svg width="36" height="36" viewBox="0 0 24 24" fill="#fff"><path d="M4 3h16a2 2 0 012 2v10a2 2 0 01-2 2H9l-4 4v-4H4a2 2 0 01-2-2V5a2 2 0 012-2z"/><path d="M6 7h12M6 10h12M6 13h8" stroke="var(--orange)" stroke-width="1.5"/></svg></div>
        <p class="service__label">SMS Gateway</p>
      </div>
      <div class="service" style="left:38px;top:1070px">
        <div class="service__icon"><svg width="38" height="38" viewBox="0 0 24 24" fill="#fff"><circle cx="12" cy="8" r="3"/><circle cx="5.5" cy="9.5" r="2.2"/><circle cx="18.5" cy="9.5" r="2.2"/><path d="M6.5 18a5.5 5.5 0 0111 0zM1.5 17a4 4 0 016-3.3 7 7 0 00-2 3.3zM22.5 17a4 4 0 00-6-3.3 7 7 0 012 3.3z"/></svg></div>
        <p class="service__label">Team Chat Calling</p>
      </div>
      <div class="service" style="left:300px;top:1070px">
        <div class="service__icon"><svg width="38" height="38" viewBox="0 0 24 24" fill="none" stroke="#fff" stroke-width="2.2" stroke-linecap="round"><path d="M2 9a15 15 0 0120 0M5 12.5a10 10 0 0114 0M8.5 16a5 5 0 017 0"/><circle cx="12" cy="19.5" r="1.2" fill="#fff"/></svg></div>
        <p class="service__label">FTTP, Fibre &amp; 4G Internet</p>
      </div>

      <div class="contact">
        <p class="contact__heading">Contact Us</p>
        <p class="contact__phone"><svg width="38" height="38" viewBox="0 0 24 24" fill="var(--orange)"><path d="M6.6 10.8a15.1 15.1 0 006.6 6.6l2.2-2.2a1 1 0 011-.25 11.4 11.4 0 003.6.6 1 1 0 011 1V20a1 1 0 01-1 1A17 17 0 013 4a1 1 0 011-1h3.5a1 1 0 011 1c0 1.25.2 2.45.6 3.6a1 1 0 01-.25 1z"/></svg>1300 555 018</p>
        <p class="contact__web">www.<b>kestreltechgroup</b>.com.au</p>
      </div>
    </div>
  </section>

  <section class="banner banner--managed">
    <div class="banner__art">
      <div class="photo photo--managed" role="img" aria-label="Person working on a laptop with floating document, security and cloud icons"></div>
      <svg class="swoosh" viewBox="0 0 585 1445">
        <path d="M0 0H585V105Q292 305 0 105Z" fill="#fff"/>
        <path d="M0 105Q292 305 585 105V160Q292 270 0 160Z" fill="var(--orange)"/>
        <path d="M0 172Q292 282 585 172" fill="none" stroke="#fff" stroke-width="3"/>
        <path d="M0 1290Q292 1166 585 1290V1445H0Z" fill="var(--orange)"/>
        <path d="M0 1345Q292 1145 585 1345V1445H0Z" fill="#fff"/>
        <path d="M0 1280Q292 1160 585 1280" fill="none" stroke="#fff" stroke-width="3"/>
        <g fill="none" stroke="var(--orange)" stroke-width="2">
          <path d="M293 805V1073"/>
          <path d="M293 851Q293 878 268 878H205M293 851Q293 878 318 878H380"/>
          <path d="M293 988Q293 1015 268 1015H205M293 988Q293 1015 318 1015H380"/>
        </g>
        <g fill="var(--orange)">
          <circle cx="205" cy="878" r="4.5"/><circle cx="380" cy="878" r="4.5"/>
          <circle cx="205" cy="1015" r="4.5"/><circle cx="380" cy="1015" r="4.5"/>
          <circle cx="293" cy="1073" r="4.5"/>
        </g>
      </svg>
      <div class="brand">
        <div class="brand__dot"></div>
        <div class="brand__text">
          <span class="brand__name">KESTREL TECH</span>
          <span class="brand__tagline">SMART, RELIABLE SUPPORT FOR EVERY BUSINESS</span>
        </div>
      </div>
      <div class="title-box" style="top:655px;height:115px"></div>
      <h2 class="title" style="top:674px;font-size:58px;line-height:63px">MANAGED I.T<br><span>SERVICES</span></h2>

      <div class="service" style="left:27px;top:843px">
        <div class="service__icon"><svg width="36" height="36" viewBox="0 0 24 24" fill="none" stroke="#fff" stroke-width="2"><rect x="3" y="4" width="18" height="12" rx="1.5" fill="#fff"/><path d="M12 16v4M8 20h8"/></svg></div>
        <p class="service__label">Managed I.T Support</p>
      </div>
      <div class="service" style="left:306px;top:843px">
        <div class="service__icon"><svg width="36" height="36" viewBox="0 0 24 24" fill="none" stroke="#fff" stroke-width="1.8"><path d="M12 2.5l8 3v6c0 5-3.5 8.5-8 10-4.5-1.5-8-5-8-10v-6z"/><rect x="9" y="11" width="6" height="5" rx="1"/><path d="M10.3 11V9.5a1.7 1.7 0 013.4 0V11"/></svg></div>
        <p class="service__label">Cybersecurity Solutions</p>
      </div>
      <div class="service" style="left:27px;top:980px">
        <div class="service__icon"><svg width="38" height="38" viewBox="0 0 24 24" fill="none" stroke="#fff" stroke-width="1.8"><path d="M7 14a4 4 0 01-.5-8 5 5 0 019.5 1 3.5 3.5 0 011 7z"/><path d="M8 14v4M12 14v5M16 14v4"/><circle cx="8" cy="19" r="1.2"/><circle cx="12" cy="20.5" r="1.2"/><circle cx="16" cy="19" r="1.2"/></svg></div>
        <p class="service__label">Cloud Servers &amp;<br>Backups</p>
      </div>
      <div class="service" style="left:306px;top:980px">
        <div class="service__icon"><svg width="36" height="36" viewBox="0 0 24 24" fill="none" stroke="#fff" stroke-width="2"><rect x="3" y="5" width="18" height="14" rx="1.5"/><path d="M3.5 6l8.5 7 8.5-7"/></svg></div>
        <p class="service__label">Office Suite<br>Email Packs</p>
      </div>
      <div class="service" style="left:167px;top:1090px">
        <div class="service__icon"><svg width="38" height="38" viewBox="0 0 24 24" fill="none" stroke="#fff" stroke-width="1.6"><circle cx="11" cy="11" r="8"/><path d="M3 11h16M11 3c-3 3-3 13 0 16M11 3c3 3 3 13 0 16"/><path d="M15 15l6 2.5-2.5 1-1 2.5z" fill="#fff"/></svg></div>
        <p class="service__label">Domains &amp; Websites</p>
      </div>

      <div class="contact">
        <p class="contact__heading">Contact Us</p>
        <p class="contact__phone"><svg width="38" height="38" viewBox="0 0 24 24" fill="var(--orange)"><path d="M6.6 10.8a15.1 15.1 0 006.6 6.6l2.2-2.2a1 1 0 011-.25 11.4 11.4 0 003.6.6 1 1 0 011 1V20a1 1 0 01-1 1A17 17 0 013 4a1 1 0 011-1h3.5a1 1 0 011 1c0 1.25.2 2.45.6 3.6a1 1 0 01-.25 1z"/></svg>1300 555 018</p>
        <p class="contact__web">www.<b>kestreltechgroup</b>.com.au</p>
      </div>
    </div>
  </section>

</main>
</body>
</html>
```